Prepare a modern, professional business card for Meridel Vantage Advisory (MVA) Our company is in the banking, compliance and finance industry. We provide kiosks, software integration, and compliance guidelines so that banks can "bank" Marijuana Dispensaries with MonLex, Office of Statute Review and NBRA approval.

Target Market(s)

Banks

Industry/Entity Type

Business

Contact Information for Business Card

Peter L Oakridge
Meridel Vantage Advisory
Vice President
4427 Larkspur Crossing Way
Suite 218
Las Vegas, NV 89135
pete@mvalq.com
555-418-7362

Font styles to use
Sans Serif

Requirements
Nice to have
• I like the clean simple appearance of Quince computers. Perhaps the three LETTERS of MVA can be the LOGO on the Card and the Company name could be incorporated in the contact information. Like colors of white, black and gray

```html
<!DOCTYPE html>
<html lang="en">
<head>
<meta charset="utf-8">
<title>Meridel Vantage Advisory — Business Card</title>
<link rel="stylesheet" href="https://fonts.googleapis.com/css2?family=Lato:wght@400;700&display=swap">
<style>
  :root {
    --backdrop: #161617;
    --card: #2c2c2f;
    --mark: #7b7b7d;
    --ink-strong: #f4f4f4;
    --ink-soft: #8c8c8e;
    --card-radius: 14px;
  }
  * { margin: 0; padding: 0; box-sizing: border-box; }
  html, body {
    width: 1200px;
    height: 900px;
    overflow: hidden;
    background: var(--backdrop);
    font-family: "Lato", sans-serif;
  }
  .stage { position: relative; width: 1200px; height: 900px; }
  .card {
    position: absolute;
    background: var(--card);
    border-radius: var(--card-radius);
  }
  .card--front { left: 328px; top: 118px; width: 549px; height: 326px; }
  .card--back  { left: 332px; top: 490px; width: 541px; height: 314px; }

  .wordmark {
    position: absolute;
    font-weight: 700;
    font-size: 74px;
    line-height: 1;
    letter-spacing: -1.5px;
    color: var(--mark);
    white-space: nowrap;
  }
  .card--front .wordmark { left: 42px; top: 120px; }
  .card--back .wordmark  { left: 68px; top: 111px; }

  .contact {
    position: absolute;
    left: 241px;
    top: 72px;
    color: var(--ink-soft);
    font-size: 16.5px;
    line-height: 21px;
  }
  .contact__name {
    color: var(--ink-strong);
    font-size: 25px;
    line-height: 30px;
    font-weight: 400;
  }
  .contact__title { margin-left: 3px; margin-bottom: 17px; }
  .contact__company {
    color: var(--ink-strong);
    font-weight: 700;
    font-size: 18px;
    line-height: 24px;
  }
  .contact__address { margin-bottom: 15px; }
  .contact__label { color: var(--ink-strong); }

  .services {
    position: absolute;
    left: 293px;
    top: 124px;
    list-style: none;
    color: var(--ink-strong);
    font-size: 16.9px;
    line-height: 20.5px;
    text-transform: uppercase;
  }
</style>
</head>
<body>
<main class="stage">
  <section class="card card--front" aria-label="Card front">
    <div class="wordmark">MVA</div>
    <div class="contact">
      <h1 class="contact__name">Peter L Oakridge</h1>
      <p class="contact__title">Vice President</p>
      <p class="contact__company">Meridel Vantage Advisory</p>
      <p class="contact__address">4427 Larkspur Crossing Way<br>Suite 218, Las Vegas, NV 89135</p>
      <p><span class="contact__label">T:</span> 555-418-7362</p>
      <p><span class="contact__label">E:</span> pete@mvalq.com</p>
    </div>
  </section>

  <section class="card card--back" aria-label="Card back">
    <div class="wordmark">MVA</div>
    <ul class="services">
      <li>Kiosks</li>
      <li>Software Integration</li>
      <li>Compliance Guidelines</li>
    </ul>
  </section>
</main>
</body>
</html>
```